Poster Design Project

Poster with modern feeling to be displayed in office. The text that needs to be included in this poster is below:

Rules
1. If it’s not in writing it doesn’t exist.
2. No such thing as 'off the record.'
3. Do not hold a private conversation in a public place.
4. Don’t believe any number that ends in zero.
5. Never turn down an opportunity to eat or go to the bathroom.
6. Don’t spend any of your own money. Don’t even admit you own a credit card. Don’t spend money that is not yours.
7. Not always a 'right' or 'wrong' answer - 'It depends.'
8. In a campaign, someone has to be in charge – campaigns are a place to foster democracy, not practice it.
9. Assume nothing.
10. If you make a mistake, fix it before analyzing. Bad news doesn’t age well.

Industry/Entity Type

Credit Card

Requirements
Must have
• Rules
7. Not always a “right” or “wrong” answer - 'It depends.' 
9. Assume nothing.

```html
<!DOCTYPE html>
<html lang="en">
<head>
<meta charset="utf-8">
<title>Rules – Office Poster</title>
<link rel="stylesheet" href="https://fonts.googleapis.com/css2?family=Marcellus&family=Pathway+Gothic+One&display=swap">
<style>
  :root {
    --paper: #e4e4e4;
    --frame-red: #d9463f;
    --frame-grey: #c9c9c9;
    --title-teal: #4f7a70;
    --body-sage: #6b8f87;
    --bloom-light: #f2f7f6;
    --bloom-mid: #bcd8d4;
  }
  html, body {
    margin: 0;
    padding: 0;
    width: 858px;
    height: 1200px;
    overflow: hidden;
    background: var(--paper);
  }
  .poster {
    position: relative;
    width: 858px;
    height: 1200px;
    box-sizing: border-box;
    background: var(--paper);
    border: 2px solid var(--frame-red);
    overflow: hidden;
  }
  .poster-inner-frame {
    position: absolute;
    inset: 2px;
    border: 2px solid var(--frame-grey);
    pointer-events: none;
  }
  .floral-corner {
    position: absolute;
    left: 0;
    bottom: 0;
    width: 420px;
    height: 300px;
  }
  .poster-title {
    position: relative;
    margin: 0;
    padding-top: 52px;
    text-align: center;
    font-family: "Marcellus", serif;
    font-weight: 400;
    font-size: 152px;
    line-height: 1;
    letter-spacing: 4px;
    color: var(--title-teal);
  }
  .rule-list {
    position: relative;
    list-style: none;
    counter-reset: rule;
    margin: 72px 0 0 0;
    padding: 0 26px 0 44px;
    font-family: "Pathway Gothic One", sans-serif;
    font-size: 37px;
    line-height: 58px;
    color: var(--body-sage);
  }
  .rule-list li {
    counter-increment: rule;
    position: relative;
    padding-left: 44px;
  }
  .rule-list li::before {
    content: counter(rule) ".";
    position: absolute;
    left: 0;
  }
  .rule-list li.rule-double-digit {
    padding-left: 56px;
  }
</style>
</head>
<body>
  <main class="poster">
    <div class="poster-inner-frame"></div>

    <svg class="floral-corner" viewBox="0 0 420 300" role="img" aria-label="Pale aqua hibiscus flower cluster decorating the lower left corner">
      <defs>
        <radialGradient id="bloom-glow" cx="0.3" cy="0.75" r="0.75">
          <stop offset="0" stop-color="var(--bloom-mid)" stop-opacity="0.85"/>
          <stop offset="0.55" stop-color="var(--bloom-light)" stop-opacity="0.6"/>
          <stop offset="1" stop-color="var(--paper)" stop-opacity="0"/>
        </radialGradient>
      </defs>
      <rect width="420" height="300" fill="url(#bloom-glow)"/>
    </svg>

    <h1 class="poster-title">RULES</h1>

    <ol class="rule-list">
      <li>If it’s not in writing it doesn’t exist.</li>
      <li>No such thing as 'off the record.'</li>
      <li>Do not hold a private conversation in a public place.</li>
      <li>Don’t believe any number that ends in zero.</li>
      <li>Never turn down an opportunity to eat or go to the bathroom.</li>
      <li>Don’t spend any of your own money. Don’t even admit you own a credit card.Don’t spend money that is not yours.</li>
      <li>Not always a 'right' or 'wrong' answer - 'It depends.'</li>
      <li>In a campaign, someone has to be in charge – campaigns are a place to foster democracy, not practice it.</li>
      <li>Assume nothing.</li>
      <li class="rule-double-digit">If you make a mistake, fix it before analyzing. Bad news doesn’t age well.</li>
    </ol>
  </main>
</body>
</html>
```